Flyer-Design für Wohn -und Einrichtungsberaterin
Zielgruppe
Ich bin eine Wohn -und Einrichtungsberaterin und biete neben der Wohnraumopitimierung auch Gartenberatung und Workshops an. Ich bin gelernte Floristin und habe daher einen engen Bezug zur Natürlichkeit.
Aufgabenstellung
Mein Flyer soll die Größe 148 x 148mm haben, mit einer klaren und ruhigen Erscheinung. Das Farbkonzept sollte sich in natürlichen und gedeckten Erdtönen wiederfinden. Trotzdem soll das Konzept ausdrucksstark präsentiert werden.
Vorderseite:
-transparentes Wohnbild im Hintergrund, darauf das Logo
-Bild (Tisch) und Logo siehe Anhänge
Rückseite:
-4 quadratische Textwürfel 2x2 angeordnet (neben- und untereinander)
1. Würfel (oben links)
Überschrift: WOHNRAUMGESTALTUNG
Text: Mit der vorhandenen Einrichtung eine Verbesserung des Wohngefühls schaffen.
2. Würfel (oben rechts)
Überschrift:GARTENBERATUNG
Text: Durch Anregung in der Garten -und Terassengestaltung ein neues Erscheinungsbild kreieren.
3. Würfel (unten links)
Überschrift: RAUMDESIGN
Text: In Praxis- und Gewerberäumen eine neue Atmosphäre erzielen.
4.Würfel (unten rechts)
Überschrift: WORKSHOPS
Text: Kreative Gruppenevents zu verschiedensten Anlässen und Themen erleben.

```html
<!DOCTYPE html>
<html lang="de">
<head>
<meta charset="utf-8">
<title>Leistungen – Wohn- und Einrichtungsberatung</title>
<link href="https://fonts.googleapis.com/css2?family=Allura&family=Lato:ital,wght@1,300;1,400&display=swap" rel="stylesheet">
<style>
  :root {
    --band: #3d2317;
    --scene-a: #5a3a2a;
    --scene-b: #6d4a36;
    --scene-c: #4a2f21;
    --tile-living: #93604a;
    --tile-garden: #83553e;
    --tile-room: #c97c5a;
    --tile-workshop: #8a5840;
    --ink: #3a1f13;
    --heading: #ffffff;
  }
  * { margin: 0; padding: 0; box-sizing: border-box; }
  html, body { width: 1200px; height: 1200px; overflow: hidden; background: var(--band); }
  .flyer-back {
    position: relative;
    width: 1200px;
    height: 1200px;
    background: var(--band);
  }
  .backdrop {
    position: absolute;
    left: 0; top: 103px;
    width: 1200px; height: 983px;
    background:
      radial-gradient(ellipse at 80% 30%, rgba(150,120,95,0.35), transparent 55%),
      radial-gradient(ellipse at 20% 70%, rgba(120,80,55,0.3), transparent 60%),
      linear-gradient(160deg, var(--scene-b), var(--scene-a) 45%, var(--scene-c));
  }
  .service-title {
    position: absolute;
    font-family: "Allura", cursive;
    font-size: 72px;
    line-height: 1;
    color: var(--heading);
    white-space: nowrap;
    z-index: 2;
  }
  .service-text {
    position: absolute;
    width: 411px;
    height: 249px;
    display: flex;
    align-items: center;
    justify-content: center;
    text-align: center;
    font-family: "Lato", sans-serif;
    font-style: italic;
    font-weight: 300;
    font-size: 29px;
    line-height: 37px;
    color: var(--ink);
    padding: 0 4px;
  }
  .service-photo {
    position: absolute;
    width: 412px;
    height: 144px;
  }
  .living .service-text { background: var(--tile-living); }
  .garden .service-text { background: var(--tile-garden); }
  .room .service-text { background: var(--tile-room); }
  .workshop .service-text { background: var(--tile-workshop); }
  .photo-windowsill { background: linear-gradient(90deg, #5b4433, #b9c2b4 40%, #c9cfc4 70%, #5e4836); }
  .photo-greenhouse { background: linear-gradient(90deg, #3f5a32, #8ea67a 45%, #5d7a47 75%, #2f4426); }
  .photo-table { background: linear-gradient(180deg, #8b7560, #b59c83 50%, #6b5140); }
  .photo-workshop { background: linear-gradient(90deg, #5d7659 22%, #e7e6e2 45%, #d9d7d2 80%, #c9b39a); }
</style>
</head>
<body>
<main class="flyer-back">
  <div class="backdrop" role="img" aria-label="Gedämpftes Foto eines Wohnraums mit Holztisch und Stühlen als Hintergrund"></div>

  <section class="service living">
    <h2 class="service-title" style="left:98px; top:145px;">Wohnraumgestaltung</h2>
    <p class="service-text" style="left:166px; top:206px;">Mit der vorhandenen<br>Einrichtung eine Verbesserung<br>des Wohngefühls<br>schaffen</p>
    <div class="service-photo photo-windowsill" style="left:166px; top:455px;" role="img" aria-label="Foto: Topfpflanzen und Kakteen auf einer Holzfensterbank"></div>
  </section>

  <section class="service garden">
    <h2 class="service-title" style="left:706px; top:145px;">Gartengestaltung</h2>
    <p class="service-text" style="left:645px; top:206px;">Durch Anregung in der<br>Garten -und Terassengestaltung<br>ein neues Erscheinungsbild<br>kreieren</p>
    <div class="service-photo photo-greenhouse" style="left:645px; top:454px;" role="img" aria-label="Foto: Grünpflanze im Gewächshaus"></div>
  </section>

  <section class="service room">
    <h2 class="service-title" style="left:98px; top:597px;">Raumdesign</h2>
    <p class="service-text" style="left:166px; top:654px;">In Praxis- und<br>Gewerberäumen eine neue<br>Atmosphäre erzielen</p>
    <div class="service-photo photo-table" style="left:166px; top:903px;" role="img" aria-label="Foto: Gedeckter Holztisch mit Windlichtern und Stühlen"></div>
  </section>

  <section class="service workshop">
    <h2 class="service-title" style="left:706px; top:597px;">Workshops</h2>
    <p class="service-text" style="left:645px; top:654px;">Kreative Gruppenevents zu<br>verschiedensten Anlässen<br>und Themen erleben</p>
    <div class="service-photo photo-workshop" style="left:645px; top:903px;" role="img" aria-label="Foto: Hände über Papierentwürfen auf einem Arbeitstisch"></div>
  </section>
</main>
</body>
</html>
```